BargoStreet Landing Page

We need a landing page for BargoStreet, which is a Deal of the day website targeting and providing daily deals to college students. The information we need on the page is as follows:
-The BargoStreet logo
-Save 50% to 90% on Great Deals Near Your College Campus and Beyond
-Enter Your Information
Email:
Location:
And a Submit button
-The footer
-We’d like to see a reference to how to earn credits for inviting friends: We are offering $50 Wandervane gift card for 10 new invites or $5 BargoStreet dollars for each invite.
If you visit www.bargostreet.com/marketing you can see our current landing page with all of the information. If you have any questions, please contact Renata at RCorvallo@bargostreet.com
Updates
We will need a Photoshop version of the final design as well.
BargoStreet has made a change to their target market, and is no longer just targeting college students. We are expanding our target market ages: 18-50+. The majority of our members will be between the ages of 18-35, so please keep that in mind when you are editing your designs. I am very sorry for the inconvenience. I will be extending the end date so there is enough time to edit. Thank you and keep up the great work!

```html
<!DOCTYPE html>
<html lang="en">
<head>
<meta charset="utf-8">
<title>BargoStreet – Save 50% to 90% on Great Deals</title>
<link href="https://fonts.googleapis.com/css2?family=Gochi+Hand&family=Arimo:wght@400;700&display=swap" rel="stylesheet">
<style>
  :root {
    --page-bg: #ececeb;
    --navy: #1e4154;
    --green: #8aab3c;
    --green-dark: #6a8a27;
    --white: #ffffff;
    --ink: #1d2b36;
    --field-border: #cfd3d6;
    --photo-a: #6f8f3f;
    --photo-b: #d9c97a;
    --card-blue: #1c4a87;
  }
  * { box-sizing: border-box; margin: 0; padding: 0; }
  html, body { width: 1200px; height: 786px; overflow: hidden; }
  body {
    position: relative;
    background: radial-gradient(ellipse at 50% 0%, #f7f7f6 0%, var(--page-bg) 60%, #e3e3e2 100%);
    font-family: "Arimo", Arial, sans-serif;
    color: var(--ink);
  }
  .brand { position: absolute; left: 84px; top: 48px; }
  .brand-name {
    font-family: "Arimo", Arial, sans-serif; font-weight: 700;
    font-size: 50px; line-height: 54px; color: var(--navy); letter-spacing: -1px;
  }
  .hero-band { position: absolute; left: 0; top: 0; width: 1200px; height: 650px; }
  .hero-photo {
    position: absolute; left: 18px; top: 246px; width: 510px; height: 384px;
    background: linear-gradient(120deg, var(--photo-a) 0%, #8fa65a 40%, var(--photo-b) 75%, #c7b56a 100%);
    opacity: .85; border-radius: 40% 40% 0 0 / 30% 30% 0 0;
  }
  .headline {
    position: absolute; left: 562px; top: 206px; color: var(--white); font-weight: 400;
    font-family: "Gochi Hand", cursive; font-size: 38px; line-height: 44px; white-space: nowrap;
  }
  .subheadline {
    position: absolute; left: 564px; top: 262px; color: var(--white); font-weight: 400;
    font-family: "Gochi Hand", cursive; font-size: 28px; line-height: 34px; white-space: nowrap;
  }
  .signup { position: absolute; left: 562px; top: 312px; }
  .signup-title { color: var(--green); font-weight: 700; font-size: 19px; margin-bottom: 14px; }
  .field {
    display: flex; align-items: center; justify-content: space-between;
    width: 238px; height: 40px; padding: 0 12px; margin-bottom: 20px;
    background: linear-gradient(#ffffff, #f1f1f1);
    border: 3px solid var(--field-border); border-radius: 9px;
    font-size: 17px; color: #222;
  }
  .field-arrows { font-size: 10px; line-height: 8px; text-align: center; }
  .submit {
    display: block; width: 120px; height: 36px; margin-top: -4px;
    border-radius: 18px; background: linear-gradient(#9cc04a, #6b8f27);
    color: var(--white); font-family: "Gochi Hand", cursive; font-size: 22px;
    text-align: center; line-height: 36px; letter-spacing: 1px;
  }
  .rewards { position: absolute; left: 568px; top: 530px; display: flex; gap: 12px; }
  .reward { width: 113px; }
  .reward-card {
    height: 66px; border: 3px solid #f4f4f4; border-radius: 7px; position: relative;
    font-weight: 700; color: var(--white);
  }
  .reward-card--partner { background: var(--card-blue); }
  .reward-card--store { background: linear-gradient(160deg, var(--green) 0 32%, #f4f4f4 32%); }
  .reward-amount { position: absolute; right: 10px; bottom: 6px; font-size: 20px; }
  .reward-card--store .reward-amount { left: 6px; top: 3px; right: auto; bottom: auto; font-size: 16px; }
  .reward-name { position: absolute; left: 6px; top: 8px; font-size: 11px; font-weight: 400; }
  .reward-card--store .reward-name { left: 30px; top: 32px; color: var(--navy); font-weight: 700; font-size: 12px; }
  .reward-note { font-size: 10px; color: var(--white); margin-top: 4px; padding-left: 2px; }
  .footer { position: absolute; left: 0; top: 650px; width: 1200px; height: 136px; }
  .footer-col { position: absolute; top: 38px; list-style: none; font-size: 14px; line-height: 17px; color: var(--ink); }
  .footer-col--social li { display: flex; align-items: center; gap: 8px; margin-bottom: 7px; line-height: 17px; }
  .icon { width: 18px; height: 17px; flex: none; }
  .footer-brand { position: absolute; left: 932px; top: 36px; text-align: right; width: 186px; }
  .footer-brand-name { font-weight: 700; font-size: 26px; color: var(--navy); text-align: center; }
  .copyright { font-size: 14px; margin-top: 14px; }
</style>
</head>
<body>
  <svg class="hero-band" viewBox="0 0 1200 650" aria-hidden="true">
    <defs>
      <linearGradient id="bandShade" x1="0" y1="0" x2="0" y2="1">
        <stop offset="0" stop-color="#2c556b"/>
        <stop offset="1" stop-color="#1b3a4c"/>
      </linearGradient>
    </defs>
    <polygon fill="#8aab3c" points="0,206 198,178 218,132 246,176 1200,70 1200,630 0,630"/>
    <polygon fill="url(#bandShade)" points="0,230 200,192 218,150 242,188 1200,88 1200,630 0,630"/>
    <rect x="0" y="630" width="1200" height="12" fill="#8aab3c"/>
  </svg>

  <header class="brand">
    <div class="brand-name">BargoStreet</div>
  </header>

  <div class="hero-photo" role="img" aria-label="Photo of two smiling young friends sitting together holding coffee mugs"></div>

  <h1 class="headline">Save 50% to 90% on Great Deals</h1>
  <h2 class="subheadline">Near Your College Campus and Beyond</h2>

  <form class="signup">
    <div class="signup-title">Enter Your Information</div>
    <div class="field">Email</div>
    <div class="field">select location <span class="field-arrows">▲<br>▼</span></div>
    <span class="submit">SUBMIT</span>
  </form>

  <section class="rewards">
    <div class="reward">
      <div class="reward-card reward-card--partner">
        <span class="reward-name">Wandervane</span>
        <span class="reward-amount">$50</span>
      </div>
      <p class="reward-note">*for 10 new invites</p>
    </div>
    <div class="reward">
      <div class="reward-card reward-card--store">
        <span class="reward-amount">$5</span>
        <span class="reward-name">BargoStreet</span>
      </div>
      <p class="reward-note">*for each invite</p>
    </div>
  </section>

  <footer class="footer">
    <ul class="footer-col" style="left:84px"><li>Daily Deal</li><li>Recent Deals</li><li>How It Works</li><li>Submit Business</li></ul>
    <ul class="footer-col" style="left:229px"><li>Feedback</li><li>Sign Up</li><li>Feature Your Business</li></ul>
    <ul class="footer-col" style="left:421px"><li>FAQs</li><li>About Us</li><li>Contact Us</li></ul>
    <ul class="footer-col" style="left:553px"><li>Legal</li><li>Our Promise</li><li>We're Hiring</li></ul>
    <ul class="footer-col footer-col--social" style="left:697px;top:40px">
      <li><svg class="icon" viewBox="0 0 18 17"><rect x="1" y="3" width="16" height="11" fill="#f4f4f4" stroke="#9a9a9a"/><polyline points="1,3 9,10 17,3" fill="none" stroke="#9a9a9a"/></svg>Contact us via Email</li>
      <li><svg class="icon" viewBox="0 0 18 17"><rect x="1" y="0" width="16" height="16" rx="2" fill="#3b5a98"/></svg>Join on Friendwall</li>
      <li><svg class="icon" viewBox="0 0 18 17"><rect x="1" y="0" width="16" height="16" rx="2" fill="#4fb6dd"/></svg>Follow us on Chirper</li>
    </ul>
    <div class="footer-brand">
      <div class="footer-brand-name">BargoStreet</div>
      <p class="copyright">© 2011 | BargoStreet.</p>
    </div>
  </footer>
</body>
</html>
```